Reel Harbor - Premier Angling Expeditions needs a one of a kind Flyer/Brochure

We need a bold, professional and confident Flyer to help us Brand and advertise what we do for companies and teams.

We Make It Easy for you to Plan Your Next Company Adventure

Reel Harbor specializes in customizing Fishing Adventures for Corporate Teams, Executive Retreats, and VIP Clients.

- Reel Harbor takes care of all the planning, preparation and logistics for all your corporate fishing adventures, so you, and your team can focus on the partnership, create stronger relationships, and enjoy the ever lasting experience these trips have to offer.
- Clients of Reel Harbor get to focus all their energy and attention on the essence of the trip and relationships with your team and leave the details of planning and logistics to Reel Harbor.
- Getting out of the office on trips like these helps create even stronger bonds with your team, customer or clients all while creating lifetime memories.
- All of our services are 100% FREE, and you never pay a dime extra for the trip.
- Service is NOT something we talk about, it's something we provide.
- We help customize the itinerary to create a balanced experience for your entire group
- What you can expect on these adventures: team building, employee retention, stronger partnerships, loyalty, growth of company culture, and good lifelong memories!
- We have Hands-on knowledge of the best Lodges for corporate retreats, team building, or exclusive VIP getaways. No matter the need we have you covered!
- What makes us so Great? There's nothing we don't do for you! We take care of everything from booking the trip, the travel, gear that’s needed, travel insurance, special food requirements, etc. And again, we do all of this for FREE!

"The backbone of our business is service and building strong relationships with our clients, outfitters, and employees….Let our team take care of your team”

Target Market(s)

Business's and Corporations

Font styles to use
Serif
Sans Serif

Colors

Designer to choose colors to be used in the design.

Requirements
Must have
• - Excellent Gammer, and a Creative flow.
• - Contact Info and social media links
• Phone: 208-555-0147
• www.reelharbor-example.com
• FB: www.facebook.com/reelharborexpeditions/
• Instagram: @reelharbor
Nice to have
• I would like the brochure to be either a tri-fold or bi-fold. I will leave that up to the designer.
• I am also up for some new design that I may not know about that looks cool and has a good flow.
Should not have
• Small, or hard to read font.

```html
<!DOCTYPE html>
<html lang="en">
<head>
<meta charset="utf-8">
<title>Reel Harbor – Corporate &amp; VIP Fishing Flyer</title>
<link href="https://fonts.googleapis.com/css2?family=Oswald:wght@400;500&family=Roboto+Condensed:wght@300;400&family=Open+Sans:wght@400;600&display=swap" rel="stylesheet">
<style>
  :root{
    --backdrop:#e4e2df;
    --paper:#f1f0ee;
    --slate:#3c4a51;
    --slate-soft:#55646b;
    --brick:#c65a47;
    --tan:#c9b39a;
    --ink:#2f3336;
    --white:#ffffff;
  }
  *{box-sizing:border-box;margin:0;padding:0}
  html,body{width:1200px;height:825px;overflow:hidden;background:var(--backdrop)}
  .canvas{position:relative;width:1200px;height:825px}
  .page{position:absolute;top:67px;width:532px;height:690px;background:var(--paper);overflow:hidden;box-shadow:0 4px 14px rgba(0,0,0,.25)}
  .page--front{left:46px}
  .page--back{left:622px}
  .waves{position:absolute;inset:0;width:532px;height:690px}
  .photo{position:absolute}
  .hero{left:0;top:0;width:532px;height:262px}
  .hero--front{background:linear-gradient(160deg,#3e5a4a 0%,#6d7f64 35%,#8f8a76 60%,#546056 100%)}
  .hero--back{background:linear-gradient(170deg,#a7b5bd 0%,#7d8f7c 35%,#5d6a5b 65%,#4a5046 100%)}
  .title{position:absolute;left:30px;top:26px;font-family:'Oswald',sans-serif;font-weight:500;font-size:24px;line-height:1.3;color:var(--white);letter-spacing:-.2px}
  .brand-mark{position:absolute;border-radius:50%;background:var(--slate);display:flex;align-items:center;justify-content:center;text-align:center;font-family:'Oswald',sans-serif;font-weight:500;color:var(--white);border:5px solid var(--slate-soft)}
  .brand-mark--front{left:74px;top:94px;width:162px;height:162px;font-size:22px}
  .brand-mark--back{left:38px;top:168px;width:144px;height:144px;font-size:20px}
  .reasons{position:absolute;left:17px;top:234px;width:287px;height:440px;background:var(--brick);color:var(--white);padding:36px 12px 0 10px}
  .reasons h2{font-family:'Open Sans',sans-serif;font-weight:400;font-size:19px;text-align:center;margin-bottom:14px}
  .reasons ul{list-style:none;font-family:'Roboto Condensed',sans-serif;font-weight:300;font-size:10.6px;line-height:1.02}
  .reasons li{position:relative;padding-left:15px;margin-bottom:6.6px}
  .reasons li::before{content:"";position:absolute;left:1px;top:2px;width:7px;height:7px;border-radius:50%;background:rgba(255,255,255,.55)}
  .pill{position:absolute;height:30px;border-radius:15px;display:flex;align-items:center;justify-content:center;gap:8px;font-family:'Open Sans',sans-serif;font-size:21px;letter-spacing:1.5px;color:var(--white)}
  .pill svg{width:20px;height:20px}
  .pill--front{left:28px;top:373px;width:224px;background:var(--slate)}
  .pill--back{left:30px;top:625px;width:224px;background:var(--brick)}
  .site{position:absolute;font-family:'Open Sans',sans-serif;font-weight:600;font-size:12.5px;letter-spacing:3px;color:var(--white)}
  .site--front{left:0;width:287px;top:414px;text-align:center;font-size:11.5px;letter-spacing:2.4px}
  .site--back{left:0;width:286px;top:664px;text-align:center;font-size:12px;letter-spacing:2.4px}
  .polaroid{position:absolute;background:var(--white);padding:7px 7px 20px;box-shadow:0 2px 6px rgba(0,0,0,.3)}
  .polaroid .shot{width:100%;height:100%}
  .pitch{position:absolute;left:316px;top:411px;width:210px;text-align:center;font-family:'Roboto Condensed',sans-serif;font-weight:300;font-size:10px;line-height:1.3;color:var(--ink)}
  .fish-art{position:absolute;left:362px;top:524px;width:120px;height:72px;border-radius:45%;background:radial-gradient(ellipse at center,#6f7a4e 0%,#8a8f63 55%,rgba(138,143,99,0) 72%)}
  .social{position:absolute;right:16px;font-family:'Roboto Condensed',sans-serif;font-weight:300;font-size:10.4px;color:var(--white);display:flex;align-items:center;gap:8px}
  .social .dot{width:14px;height:14px;border-radius:50%;background:var(--white)}
  .social--fb{top:640px}
  .social--ig{top:660px}
  .section-title{position:absolute;left:22px;top:322px;font-family:'Oswald',sans-serif;font-weight:500;font-size:24px;color:var(--brick);letter-spacing:-.3px}
  .quote{position:absolute;left:25px;width:334px;font-family:'Roboto Condensed',sans-serif;font-weight:300;font-size:10.8px;line-height:1.28;color:var(--ink)}
  .quote::before{content:"\201C";font-family:'Oswald',sans-serif;font-size:36px;line-height:0;color:#b9b9b9;vertical-align:-14px;margin-right:6px}
  .quote--1{top:368px}
  .quote--2{top:427px}
  .quote--3{top:497px}
</style>
</head>
<body>
<main class="canvas">

  <section class="page page--front" aria-label="Front page">
    <div class="photo hero hero--front" role="img" aria-label="Smiling angler in waders holding a trout beside a river"></div>
    <svg class="waves" viewBox="0 0 532 690" aria-hidden="true">
      <path d="M0 232 C150 272 330 252 532 186 L532 204 C330 272 150 292 0 252Z" fill="var(--slate)"/>
      <path d="M0 250 C150 290 330 270 532 202 L532 218 C330 284 150 304 0 266Z" fill="var(--tan)"/>
      <path d="M0 264 C150 302 330 282 532 216 L532 690 L0 690Z" fill="var(--paper)"/>
      <path d="M0 548 C150 590 360 510 532 556 L532 566 C360 522 150 602 0 560Z" fill="var(--tan)"/>
      <path d="M0 558 C150 600 360 520 532 564 L532 690 L0 690Z" fill="var(--slate)"/>
    </svg>
    <h1 class="title">REEL HARBOR'S CORPORATE &amp;<br>VIP FISHING ADVENTURES</h1>
    <div class="brand-mark brand-mark--front">Reel Harbor</div>

    <div class="reasons">
      <h2>Why Fish With Reel Harbor?</h2>
      <ul>
        <li>Reel Harbor is a booking agency for fishing adventures around the world.</li>
        <li>All of our services are 100% FREE, and you never pay a dime extra for the trip.</li>
        <li>We can customize each trip to fit your specific needs and requirements.</li>
        <li>Huge advantage of working with Reel Harbor is that we have access to the best dates, and discounts.</li>
        <li>Nobody can beat our prices or deals.</li>
        <li>Nobody cares or has more hands-on knowledge of the best lodges.</li>
        <li>Lodges roll out the red carpet for our clients</li>
        <li>Reel Harbor specializes in the most unique and memorable fishing adventures for corporate teams, and VIP clients.</li>
        <li>We create proper expectations, and then exceed from there.</li>
        <li>We take care of all the little details; Special food requirements, travel, gear, travel insurance, etc.</li>
        <li>We plan so you don't have to.</li>
      </ul>
      <div class="pill pill--front">
        <svg viewBox="0 0 24 24" aria-hidden="true"><circle cx="12" cy="12" r="10" fill="none" stroke="#fff" stroke-width="2"/><path d="M8.5 7.5c.6-.6 1.4-.5 1.8.1l.9 1.4c.3.5.2 1.1-.2 1.5l-.6.6c.6 1.3 1.5 2.2 2.8 2.8l.6-.6c.4-.4 1-.5 1.5-.2l1.4.9c.6.4.7 1.2.1 1.8l-.7.7c-2.8.6-7.9-4.5-7.3-7.3z" fill="#fff"/></svg>
        208-555-0147
      </div>
      <div class="site site--front">www.reelharbor-example.com</div>
    </div>

    <div class="polaroid" style="left:300px;top:262px;width:140px;height:128px;transform:rotate(-5deg)">
      <div class="shot" role="img" aria-label="Angler in a boat on a turquoise river gorge" style="background:linear-gradient(160deg,#3d6b4a,#2fa3a0 55%,#3a5a45)"></div>
    </div>
    <div class="polaroid" style="left:418px;top:240px;width:112px;height:112px;transform:rotate(6deg)">
      <div class="shot" role="img" aria-label="Group of anglers with a row of caught salmon at a dock" style="background:linear-gradient(170deg,#8b949a,#5f6a6e 55%,#c9cccc)"></div>
    </div>

    <p class="pitch">We only believe in World Class Fishing! The adventure starts with the right location that fits you best! Reel Harbor helps research, book and plan fishing trips with the best guides and fishing lodges in the world. Our full-time consultants only recommend the best guided trips. That's our business, and our advice is free.</p>
    <div class="fish-art" role="img" aria-label="Illustration of a leaping largemouth bass"></div>

    <div class="social social--fb">www.facebook.com/reelharborexpeditions/ <span class="dot"></span></div>
    <div class="social social--ig">@reelharbor <span class="dot"></span></div>
  </section>

  <section class="page page--back" aria-label="Back page">
    <div class="photo hero hero--back" role="img" aria-label="Two smiling anglers holding a large steelhead in a river"></div>
    <svg class="waves" viewBox="0 0 532 690" aria-hidden="true">
      <path d="M0 300 C120 250 260 300 532 236 L532 690 L0 690Z" fill="var(--paper)"/>
      <path d="M0 548 C160 585 360 512 532 548 L532 690 L0 690Z" fill="var(--slate)"/>
      <path d="M170 582 C300 560 420 548 532 560 L532 568 C420 556 300 566 170 582Z" fill="var(--paper)" opacity=".7"/>
    </svg>
    <div class="brand-mark brand-mark--back">Reel Harbor</div>

    <h2 class="section-title">TAILS FROM THE WATER:</h2>
    <p class="quote quote--1">Unbelievable team at Reel Harbor! Details are the key when planning a trip of a lifetime and these guys have the details dialed. Gavin Roarke Host of Open Current Outdoors TV Show</p>
    <p class="quote quote--2">Marcus and Reel Harbor are the real deal. They combine excellent customer service with a true understanding of angling travel issues. I just completed a trip to Russia arranged by Marcus and Reel Harbor and I would highly recommend their services to anyone! Wes Tolland</p>
    <p class="quote quote--3">Great company with fantastic people and service! Highly recommend! Nora Vell Owner of Larkspur Travel Boutique</p>

    <div class="polaroid" style="left:352px;top:185px;width:178px;height:145px;transform:rotate(6deg)">
      <div class="shot" role="img" aria-label="Angler in a bright jacket holding a fish over open water" style="background:linear-gradient(170deg,#9fb8cf,#4d7a9a 50%,#2f5674)"></div>
    </div>
    <div class="polaroid" style="left:360px;top:327px;width:170px;height:140px;transform:rotate(-3deg)">
      <div class="shot" role="img" aria-label="Group beside a floatplane under a blue sky" style="background:linear-gradient(175deg,#3f78c2,#9dbbe0 45%,#6f6a5c)"></div>
    </div>
    <div class="polaroid" style="left:372px;top:478px;width:158px;height:148px;transform:rotate(6deg)">
      <div class="shot" role="img" aria-label="Anglers on a boat deck with their catch" style="background:linear-gradient(170deg,#7f8c95,#4c555b 50%,#dcdfe0)"></div>
    </div>

    <div class="pill pill--back">
      <svg viewBox="0 0 24 24" aria-hidden="true"><circle cx="12" cy="12" r="10" fill="none" stroke="#fff" stroke-width="2"/><path d="M8.5 7.5c.6-.6 1.4-.5 1.8.1l.9 1.4c.3.5.2 1.1-.2 1.5l-.6.6c.6 1.3 1.5 2.2 2.8 2.8l.6-.6c.4-.4 1-.5 1.5-.2l1.4.9c.6.4.7 1.2.1 1.8l-.7.7c-2.8.6-7.9-4.5-7.3-7.3z" fill="#fff"/></svg>
      208-555-0147
    </div>
    <div class="site site--back">www.reelharbor-example.com</div>

    <div class="social social--fb">www.facebook.com/reelharborexpeditions/ <span class="dot"></span></div>
    <div class="social social--ig">@reelharbor <span class="dot"></span></div>
  </section>

</main>
</body>
</html>
```